Thornbury Sisters need Sticker designs to promote their history

Perth Thornbury Sisters is a group of Commonweal Party Western Australia, first established in 1912. The achievements of Thornbury Sisters in Australia are historical, and we would like to promote our achievements. We would like to raise money by designing a set of stickers. A similar campaign was conducted by HARRIET's Circle USA. We would like to see designs that use the colours of red, purple and white. Designs can take inspiration from the political posters of the 1930s and need to easy to read.

Target Market(s)

Australian women - young, old

Industry/Entity Type

Political

Font styles to use
Serif
Sans Serif

Colors
ec2027
6b449b
ffffff

Requirements
Must have
• Must be able to be read in one go.
Nice to have
• Outline of Australian Assembly Hall
Should not have
• Too many colours

```html
<!DOCTYPE html>
<html lang="en">
<head>
<meta charset="utf-8">
<title>Thornbury Sisters Stickers</title>
<link rel="stylesheet" href="https://fonts.googleapis.com/css2?family=Jost:wght@500;600;700;800&family=Lobster+Two:ital,wght@1,700&display=swap">
<style>
  :root {
    --red: #ec2027;
    --purple: #6b449b;
    --white: #ffffff;
    --black: #0a0a0a;
    --frame: #9a9a9a;
    --sans: "Jost", "Futura", Arial, sans-serif;
    --script: "Lobster Two", "Georgia", cursive;
  }
  * { margin: 0; padding: 0; box-sizing: border-box; }
  html, body { width: 1033px; height: 1200px; overflow: hidden; background: var(--white); }
  .sheet {
    position: relative;
    width: 1033px; height: 1200px;
    border: 2px solid var(--frame);
    background: var(--white);
  }
  .sticker {
    position: absolute;
    left: 72px; width: 897px; height: 326px;
    overflow: hidden;
    font-family: var(--sans);
    color: var(--white);
  }
  .sticker--join { top: 53px; background: var(--red); }
  .sticker--vote { top: 436px; background: var(--purple); }
  .sticker--more { top: 816px; background: var(--red); }
  .band { position: absolute; inset: 0; width: 897px; height: 326px; }
  .script { position: absolute; font-family: var(--script); font-style: italic; font-weight: 700; white-space: nowrap; transform-origin: left bottom; line-height: 1; }
  .script--light { color: var(--white); }
  .script--dark { color: var(--black); }

  /* JOIN */
  .honour-roll {
    position: absolute; left: 0; top: 0; width: 314px; height: 326px;
    background: var(--black);
    text-align: right; text-transform: uppercase;
    list-style: none;
  }
  .honour-roll li { position: absolute; right: 26px; }
  .honour-roll .name { display: block; font-weight: 700; font-size: 16px; letter-spacing: .4px; line-height: 1.2; }
  .honour-roll .role { display: block; font-weight: 700; font-size: 10px; line-height: 1.15; }
  .headline { position: absolute; font-weight: 800; text-transform: uppercase; line-height: .8; white-space: nowrap; }
  .join-word { left: 372px; top: 126px; font-size: 136px; letter-spacing: 8px; }
  .join-sub { position: absolute; left: 403px; top: 262px; width: 346px; text-align: center; font-weight: 700; text-transform: uppercase; font-size: 18px; line-height: 1.3; letter-spacing: 1.5px; white-space: nowrap; }

  /* VOTE */
  .policy-list { position: absolute; right: 19px; top: 94px; text-align: right; text-transform: uppercase; font-weight: 700; font-size: 18px; line-height: 31px; letter-spacing: 1.4px; list-style: none; white-space: nowrap; }
  .vote-word { right: 18px; top: 262px; font-size: 59px; letter-spacing: 0; }

  /* MORE */
  .more-word { right: 38px; top: 123px; font-size: 103px; letter-spacing: 0; }
  .more-sub { position: absolute; right: 33px; top: 205px; text-align: right; text-transform: uppercase; font-weight: 700; font-size: 27px; line-height: 30px; letter-spacing: 3px; white-space: nowrap; }
</style>
</head>
<body>
<main class="sheet">

  <section class="sticker sticker--join">
    <svg class="band" viewBox="0 0 897 326" role="img" aria-label="Line drawing of Australian Assembly Hall on a white diagonal band">
      <defs><linearGradient id="hallJoin" x1="0" y1="0" x2="1" y2="1"><stop offset="0" stop-color="#ffffff"/><stop offset="1" stop-color="#e6e6e6"/></linearGradient></defs>
      <polygon points="440,0 540,0 897,150 897,300" fill="url(#hallJoin)"/>
    </svg>
    <ul class="honour-roll">
      <li style="top:30px"><span class="name">Margaret Ellery</span><span class="role">(1st female Commonweal senator)</span></li>
      <li style="top:91px"><span class="name">Edith Varley</span><span class="role">(1st female speaker of the house)</span></li>
      <li style="top:141px"><span class="name">Rosalind Carver</span><span class="role">(1st female leader of the<br>Australian Assembly)</span></li>
      <li style="top:204px"><span class="name">Maree Bindon</span><span class="role">(1st female Aboriginal<br>member of parliament)</span></li>
      <li style="top:254px"><span class="name">Helen Ashcombe</span><span class="role">(1st female prime minister of<br>Australia)</span></li>
    </ul>
    <p class="script script--light" style="left:640px; top:8px; font-size:30px; transform:rotate(18deg);">Thornbury Sisters</p>
    <p class="script script--dark" style="left:628px; top:63px; font-size:34px; transform:rotate(18deg);">make History</p>
    <h2 class="headline join-word">Join</h2>
    <p class="join-sub">Perth Thornbury Sisters.<br>Be part of a shared history.</p>
  </section>

  <section class="sticker sticker--vote">
    <svg class="band" viewBox="0 0 897 326" role="img" aria-label="Line drawing of Australian Assembly Hall on a white diagonal band">
      <defs><linearGradient id="hallVote" x1="0" y1="1" x2="1" y2="0"><stop offset="0" stop-color="#ffffff"/><stop offset="1" stop-color="#e6e6e6"/></linearGradient></defs>
      <polygon points="0,240 497,0 518,0 115,326 0,326" fill="url(#hallVote)"/>
    </svg>
    <p class="script script--light" style="left:14px; top:209px; font-size:31px; transform:rotate(-26deg);">Commonweal Has Provided Women</p>
    <p class="script script--dark" style="left:22px; top:252px; font-size:44px; transform:rotate(-29deg);">Equal Opportunity</p>
    <ul class="policy-list">
      <li>Childcare</li>
      <li>Pay equity</li>
      <li>Support of domestic violence refuges</li>
      <li>Superannuation for women</li>
      <li>Single parent pension</li>
    </ul>
    <h2 class="headline vote-word">Vote Commonweal.</h2>
  </section>

  <section class="sticker sticker--more">
    <svg class="band" viewBox="0 0 897 326" role="img" aria-label="Line drawing of Australian Assembly Hall on a white diagonal band">
      <defs><linearGradient id="hallMore" x1="0" y1="1" x2="1" y2="0"><stop offset="0" stop-color="#ffffff"/><stop offset="1" stop-color="#e6e6e6"/></linearGradient></defs>
      <polygon points="40,326 560,0 600,0 270,326" fill="url(#hallMore)"/>
    </svg>
    <p class="script script--light" style="left:36px; top:244px; font-size:56px; transform:rotate(-33deg);">Thornbury Sisters</p>
    <p class="script script--dark" style="left:101px; top:262px; font-size:52px; transform:rotate(-33deg);">make History</p>
    <h2 class="headline more-word">More</h2>
    <p class="more-sub">Women in the house<br>and the senate<br>and in the cabinet.</p>
  </section>

</main>
</body>
</html>
```